Visitenkarten für regionale Fluggesellschaft
Zielgruppe
Wir sind eine regionale Fluggesellschaft, die seit zehn Jahren Flüge von Mannheim aus anbietet.
Aufgabenstellung
Gern möchten wir das Design der bisherigen Visitenkarten überarbeiten lassen. Die bisherigen sind seit über fünf Jahren im Einsatz. Es darf moderner aussehen. Vielleicht auch mit Symbolen (wie Font Awesome) gearbeitet werden.
Die Adresse sollte sein:
LHV Lindenhof-Vogtmar Jet GmbH
Birkenweiler Talstr. 48
74391 Mannheim

```html
<!DOCTYPE html>
<html lang="de">
<head>
<meta charset="utf-8">
<title>Visitenkarten – Lindenhof-Vogtmar Jet</title>
<link href="https://fonts.googleapis.com/css2?family=Open+Sans:wght@400;600;700&display=swap" rel="stylesheet">
<style>
  :root {
    --bg: #eceeef;
    --card: #ffffff;
    --blue: #2b8fd8;
    --blue-light: #8cc4ec;
    --yellow: #e3d21c;
    --green-light: #8dbf3b;
    --green: #1f9a4c;
    --ink: #3a3d40;
  }
  * { box-sizing: border-box; margin: 0; padding: 0; }
  html, body { width: 1200px; height: 721px; overflow: hidden; }
  body {
    background: var(--bg);
    font-family: "Open Sans", sans-serif;
    color: var(--ink);
    position: relative;
  }
  .card {
    position: absolute;
    top: 192px;
    width: 520px;
    height: 336px;
    background: var(--card);
    box-shadow: 0 6px 18px rgba(0,0,0,0.12);
    overflow: hidden;
  }
  .card--contact { left: 50px; }
  .card--brand { left: 630px; }

  .decor { position: absolute; }
  .card--contact .decor--corner {
    left: 0; bottom: 0;
    width: 210px; height: 150px;
    background: linear-gradient(135deg, var(--blue-light) 0%, var(--blue) 55%, var(--yellow) 100%);
    opacity: 0.9;
  }
  .card--brand .decor--edge {
    right: 0; top: 0;
    width: 110px; height: 100%;
    background: linear-gradient(180deg, var(--blue-light) 0%, var(--blue) 60%, var(--yellow) 100%);
    opacity: 0.9;
  }
  .card--brand .decor--corner {
    left: 0; bottom: 0;
    width: 70px; height: 95px;
    background: linear-gradient(180deg, var(--green-light) 0%, var(--green) 100%);
  }

  .wordmark {
    position: absolute;
    display: flex;
    align-items: center;
    gap: 8px;
    color: var(--blue);
    font-weight: 600;
    white-space: nowrap;
  }
  .wordmark__square { width: 12px; height: 12px; background: var(--blue); }
  .card--contact .wordmark { left: 36px; top: 70px; font-size: 17px; }

  .contact {
    position: absolute;
    left: 262px;
    top: 58px;
    font-size: 12.5px;
    line-height: 1.42;
  }
  .contact__name {
    color: var(--blue);
    font-weight: 700;
    font-size: 18px;
    letter-spacing: 0.02em;
    line-height: 1.1;
  }
  .contact__role { margin-bottom: 12px; }
  .contact__address { margin-bottom: 10px; }
  .contact__line { display: flex; align-items: center; gap: 8px; }
  .contact__line svg { width: 12px; height: 12px; flex: none; }

  .card--brand .wordmark {
    left: 0; right: 110px; top: 150px;
    justify-content: center;
    font-size: 24px;
  }
  .web {
    position: absolute;
    left: 0; right: 110px; bottom: 22px;
    text-align: center;
    color: var(--blue);
    font-size: 13px;
  }
</style>
</head>
<body>

<section class="card card--contact" aria-label="Visitenkarte Rückseite mit Kontaktdaten">
  <div class="decor decor--corner" role="img" aria-label="Dekorative Farbfläche in Blau und Gelb"></div>

  <div class="wordmark"><span class="wordmark__square"></span>Lindenhof-Vogtmar Jet</div>

  <div class="contact">
    <p class="contact__name">TOBIAS QUINT</p>
    <p class="contact__role">Chief Commercial Officer</p>
    <p class="contact__address">LHV Lindenhof-Vogtmar Jet GmbH<br>Birkenweiler Talstr. 48<br>74391 Mannheim</p>
    <p class="contact__line">
      <svg viewBox="0 0 16 16" aria-hidden="true"><path d="M3 1h3l1.5 4-2 1.2a9 9 0 0 0 4.3 4.3L11 8.5l4 1.5v3a2 2 0 0 1-2 2A12 12 0 0 1 1 3a2 2 0 0 1 2-2z" fill="var(--ink)"/></svg>
      +49 (0) 621 57 19 40 - 0
    </p>
    <p class="contact__line">
      <svg viewBox="0 0 16 16" aria-hidden="true"><rect x="4" y="1" width="8" height="14" rx="1.5" fill="none" stroke="var(--ink)" stroke-width="1.6"/><circle cx="8" cy="12.5" r="0.9" fill="var(--ink)"/></svg>
      +49 (0) 176 208 613 95
    </p>
    <p class="contact__line">
      <svg viewBox="0 0 16 16" aria-hidden="true"><rect x="1" y="3" width="14" height="10" fill="none" stroke="var(--ink)" stroke-width="1.4"/><path d="M1 3l7 6 7-6" fill="none" stroke="var(--ink)" stroke-width="1.4"/></svg>
      tobias.quint@flylhv.com
    </p>
  </div>
</section>

<section class="card card--brand" aria-label="Visitenkarte Vorderseite">
  <div class="decor decor--edge" role="img" aria-label="Dekorative Farbfläche in Blau und Gelb"></div>
  <div class="decor decor--corner" role="img" aria-label="Dekorative Farbfläche in Grün"></div>

  <div class="wordmark"><span class="wordmark__square"></span>Lindenhof-Vogtmar Jet</div>
  <p class="web">www.flyLHV.com</p>
</section>

</body>
</html>
```